Marigold Rest Pet Cremation, Client catalog

Marigold rest is a Pet crematorium in Melbourne, Aus. This catalogue is to show clients our services , as well as our range of urns, jewellery and keepsake items. Marigold rest provides services for all pets, focusing on exotics, such as rabbits, Guinea pigs, snakes and birds.
- the layout will have pictures with space to add text that will include size and price.
The main colour is N460 After rain with HDC-MD- 08 whisper white, MQ3-27 etched glass and S180-2 sunwashed brick.
Updates

Designs look the same

Target Market(s)

All pet owners

Industry/Entity Type

Funeral, crematorium for Pets

Font styles to use
Script

Colors
0094D4
00A9DD
6FCCEA
C7EBF8
E9F6FB

Requirements
Must have
• Allowing me to upload pictures of items and corresponding price info as needed
Nice to have
• Boho vibes. pastel colour scheme, clean, modern layout.
Should not have
• Paw print symbols and/or love heart symbols. Typical dark, sad vibe. Info overload. It’s a catalog not a brochure

```html
<!DOCTYPE html>
<html lang="en">
<head>
<meta charset="utf-8">
<title>Marigold Rest Pet Cremation – Client Catalog</title>
<link rel="stylesheet" href="https://fonts.googleapis.com/css2?family=Lora:ital,wght@1,400&family=Poppins:ital,wght@0,400;0,500;1,800&family=Yellowtail&display=swap">
<style>
  :root{
    --stage:#1c1c1e;
    --after-rain:#0094D4;
    --sky:#00A9DD;
    --etched:#6FCCEA;
    --mist:#C7EBF8;
    --whisper:#E9F6FB;
    --band:#dbeff3;
    --white:#ffffff;
    --ink:#1b1b1b;
    --body:#3a3a3a;
    --muted:#6a7780;
  }
  *{margin:0;padding:0;box-sizing:border-box}
  html,body{width:1029px;height:1200px;overflow:hidden;background:var(--stage)}
  .canvas{position:relative;width:1029px;height:1200px;background:var(--stage);font-family:"Poppins",sans-serif}
  .abs{position:absolute}

  /* cover spread */
  .cover-spread{left:154px;top:71px;width:720px;height:509px;background:var(--band);overflow:hidden}
  .front-page-top{left:0;top:0;width:360px;height:304px;background:var(--white)}
  .photo-dog-grass{left:17px;top:17px;width:326px;height:372px;
    background:linear-gradient(160deg,#6f7a3e 0%,#8fae4a 35%,#b9c98a 55%,#e8e3d6 70%,#7f9a3a 100%)}
  .photo-owner-dog{left:360px;top:0;width:360px;height:304px;
    background:linear-gradient(170deg,#6b6a45 0%,#c9a35a 30%,#e2c27a 55%,#f0ebe1 70%,#d1a45a 100%)}
  .remember-badge{left:466px;top:241px;width:148px;height:148px;border-radius:50%;background:var(--white)}
  .bouquet{left:52px;top:12px;width:44px;height:62px;border-radius:50%;
    background:radial-gradient(circle,#e6c9c9 0%,#7b8a7c 70%,transparent 72%)}
  .remember-text{left:0;top:74px;width:148px;text-align:center;font-family:"Lora",serif;font-style:italic;
    color:var(--after-rain);font-size:20px;line-height:20px;letter-spacing:.3px}
  .brand-name{width:360px;top:424px;text-align:center;font-family:"Yellowtail",cursive;font-weight:400;
    font-size:28px;line-height:34px;color:var(--ink);white-space:nowrap}
  .brand-left{left:0}
  .brand-right{left:360px}

  /* inner spread */
  .inner-spread{left:154px;top:620px;width:720px;height:509px;overflow:hidden;background:var(--white)}
  .photo-blue-side{top:0;width:44px;height:509px;
    background:linear-gradient(180deg,#0a63b5 0%,#1f86d6 40%,#0b5aa8 70%,#2b8fe0 100%)}
  .side-left{left:0}
  .side-right{left:317px}
  .story-panel{left:44px;top:0;width:273px;height:509px;background:var(--whisper)}
  .portrait-ring{left:22px;top:35px;width:228px;height:228px;border-radius:50%;border:1px solid var(--etched)}
  .portrait-photo{left:7px;top:7px;width:212px;height:212px;border-radius:50%;
    background:radial-gradient(circle at 50% 55%,#f3efe6 0%,#d9cdb8 35%,#8f8a6a 70%,#5f6a4a 100%)}
  .pet-name{left:0;top:279px;width:273px;text-align:center;font-weight:800;font-style:italic;
    color:var(--after-rain);font-size:14px;letter-spacing:-.2px}
  .story-text{left:30px;top:312px;width:216px;font-size:5.8px;line-height:10.6px;color:var(--body)}
  .story-text p{margin-bottom:10.6px}

  .catalog-page{left:360px;top:0;width:360px;height:509px;background:var(--white)}
  .catalog-band{left:0;top:0;width:360px;height:79px;background:var(--after-rain)}
  .catalog-frame{left:35px;top:35px;width:292px;height:441px;border:1px solid var(--etched)}
  .section-title{left:11px;top:16px;color:var(--white);font-weight:800;font-style:italic;font-size:10.5px;letter-spacing:.3px}
  .product-grid{left:10px;top:60px;display:grid;grid-template-columns:repeat(3,84px);grid-auto-rows:122px;column-gap:9px}
  .product-item{display:flex;flex-direction:column}
  .product-slot{width:84px;height:79px;border:1px solid #e6e6e6}
  .product-caption{margin-top:5px;font-size:6.5px;line-height:9px;color:var(--body)}
  .product-caption .item-name{display:block;font-weight:500;color:var(--after-rain)}
  .product-caption .item-meta{display:block;color:var(--muted)}
  .item-beads{background:linear-gradient(135deg,#eeeef0 0%,#8b7a66 45%,#e8e8ea 100%)}
  .item-box{background:radial-gradient(ellipse at 50% 50%,#1d1d1d 0%,#6b5a3c 35%,#ffffff 62%)}
  .item-vase{background:radial-gradient(ellipse 30% 48% at 50% 50%,#eadfd6 0%,#d8b7b0 60%,#ffffff 100%)}
</style>
</head>
<body>
<div class="canvas">

  <section class="abs cover-spread">
    <div class="abs front-page-top"></div>
    <div class="abs photo-dog-grass" role="img" aria-label="Photo of a white dog lying on grass in a park"></div>
    <div class="abs photo-owner-dog" role="img" aria-label="Photo of a woman hugging her white dog among autumn leaves"></div>
    <div class="abs remember-badge">
      <div class="abs bouquet" role="img" aria-label="Illustration of a small flower bouquet"></div>
      <p class="abs remember-text">WE WILL<br>REMEMBER<br>YOU.</p>
    </div>
    <p class="abs brand-name brand-left">Marigold Rest Pet Cremation</p>
    <p class="abs brand-name brand-right">Marigold Rest Pet Cremation</p>
  </section>

  <section class="abs inner-spread">
    <div class="abs photo-blue-side side-left" role="img" aria-label="Blue-toned photo of a person with a dog"></div>
    <div class="abs photo-blue-side side-right" role="img" aria-label="Blue-toned photo of a person with a dog"></div>
    <article class="abs story-panel">
      <div class="abs portrait-ring">
        <div class="abs portrait-photo" role="img" aria-label="Round photo of a white dog on a forest path"></div>
      </div>
      <h2 class="abs pet-name">PET NAME PET NAME</h2>
      <div class="abs story-text">
        <p>Lorem ipsum dolor sit amet, consectetur adipiscing elit. Integer nisl libero, imperdiet ac efficitur quis, tempor vestibulum est. Phasellus vitae odio porttitor justo commodo sagittis. Nulla ante ligula, pharetra ac lacus at, lacinia volutpat dui. Aenean mauris massa, imperdiet vitae aliquet in, condimentum quis quam. Suspendisse vehicula arcu vitae orci sagittis dictum.</p>
        <p>Aliquam a vehicula turpis. Vestibulum feugiat lacus felis, ac venenatis nulla auctor in. Nullam non sagittis felis, non luctus ex. Phasellus sodales enim vel metus dapibus consectetur. Phasellus ullamcorper sem non nisl consectetur, at ultrices nisi cursus. Mauris viverra luctus augue, sit amet egestas ante sollicitudin ut.</p>
        <p>Aliquam felis felis, pulvinar sit amet eleifend non, pellentesque sodales nisl. Integer et rhoncus leo, nec consequat nisi. Morbi non tellus diam. Morbi lacus turpis, viverra eget pulvinar vel, aliquam non mi.</p>
      </div>
    </article>

    <article class="abs catalog-page">
      <div class="abs catalog-band"></div>
      <div class="abs catalog-frame">
        <h2 class="abs section-title">ACCESSORIES</h2>
        <div class="abs product-grid">
          <figure class="product-item">
            <div class="product-slot item-beads" role="img" aria-label="Photo of beaded bracelets"></div>
            <figcaption class="product-caption"><span class="item-name">Beaded Bracelet</span><span class="item-meta">Size 18 cm · $45</span></figcaption>
          </figure>
          <figure class="product-item">
            <div class="product-slot item-box" role="img" aria-label="Photo of an open mosaic keepsake box"></div>
            <figcaption class="product-caption"><span class="item-name">Keepsake Box</span><span class="item-meta">Size 12 cm · $85</span></figcaption>
          </figure>
          <figure class="product-item">
            <div class="product-slot item-vase" role="img" aria-label="Photo of a floral porcelain urn"></div>
            <figcaption class="product-caption"><span class="item-name">Porcelain Urn</span><span class="item-meta">Size 25 cm · $120</span></figcaption>
          </figure>
          <figure class="product-item">
            <div class="product-slot item-beads" role="img" aria-label="Photo of beaded bracelets"></div>
            <figcaption class="product-caption"><span class="item-name">Beaded Bracelet</span><span class="item-meta">Size 18 cm · $45</span></figcaption>
          </figure>
          <figure class="product-item">
            <div class="product-slot item-box" role="img" aria-label="Photo of an open mosaic keepsake box"></div>
            <figcaption class="product-caption"><span class="item-name">Keepsake Box</span><span class="item-meta">Size 12 cm · $85</span></figcaption>
          </figure>
          <figure class="product-item">
            <div class="product-slot item-vase" role="img" aria-label="Photo of a floral porcelain urn"></div>
            <figcaption class="product-caption"><span class="item-name">Porcelain Urn</span><span class="item-meta">Size 25 cm · $120</span></figcaption>
          </figure>
          <figure class="product-item">
            <div class="product-slot item-beads" role="img" aria-label="Photo of beaded bracelets"></div>
            <figcaption class="product-caption"><span class="item-name">Beaded Bracelet</span><span class="item-meta">Size 18 cm · $45</span></figcaption>
          </figure>
          <figure class="product-item">
            <div class="product-slot item-box" role="img" aria-label="Photo of an open mosaic keepsake box"></div>
            <figcaption class="product-caption"><span class="item-name">Keepsake Box</span><span class="item-meta">Size 12 cm · $85</span></figcaption>
          </figure>
          <figure class="product-item">
            <div class="product-slot item-vase" role="img" aria-label="Photo of a floral porcelain urn"></div>
            <figcaption class="product-caption"><span class="item-name">Porcelain Urn</span><span class="item-meta">Size 25 cm · $120</span></figcaption>
          </figure>
        </div>
      </div>
    </article>
  </section>

</div>
</body>
</html>
```